Business Card Design For Office Furniture Clearance Company

Kestrel Office Clearance - our company name pretty much explains what we do, we clear offices for high end clients, mainly plc's and large international companies.

We require a nice looking business card that displays professionalism but without being too serious.

It would be nice to see just a little more than a conventional boring business card, make sure you add some flare.

Industry/Entity Type

Office Furniture

Contact Information for Business Card

CARD 1

Tom Pardew
Director
tom@kestrelofficeclearance.co.uk
m: 07700 513928

t: 01632 419063
www.kestrelofficeclearance.co.uk

Kestrel Office Clearance
Unit K4 B
3-7 Ferndale Lane
Harwick
Linmoor Vale
ZZ9 4QX

free office clearances… hard to beat that, really.

CARD 2

Henry Walbrook
Director
henry@kestrelofficeclearance.co.uk
m: 07700 628157

t: 01632 419063

Kestrel Office Clearance
Unit K4 B
3-7 Ferndale Lane
Harwick
Linmoor Vale
ZZ9 4QX

Font styles to use
Sans Serif

Requirements
Must have
• A white background - as we have a blue logo.
Nice to have
• Nice use of the logo - play around with this and dissect it.

```html
<!DOCTYPE html>
<html lang="en">
<head>
<meta charset="utf-8">
<title>Kestrel Office Clearance – Business Cards</title>
<link rel="stylesheet" href="https://fonts.googleapis.com/css2?family=Abel&family=Didact+Gothic&family=Reenie+Beanie&display=swap">
<style>
  :root {
    --backdrop-light: #f4f4f4;
    --backdrop-dark: #a9a7a8;
    --card-white: #ffffff;
    --brand-blue: #0a72b8;
    --name-blue: #1f6aa5;
    --pale-blue: #b5d5e8;
    --ink: #2b2b2b;
    --muted: #8a8a8a;
  }
  * { margin: 0; padding: 0; box-sizing: border-box; }
  html, body { width: 1200px; height: 786px; overflow: hidden; }
  body {
    background: linear-gradient(110deg, var(--backdrop-light) 0%, #dcdcdc 55%, var(--backdrop-dark) 100%);
    position: relative;
    font-family: "Didact Gothic", sans-serif;
  }
  .card {
    position: absolute;
    width: 520px;
    height: 338px;
    background: var(--card-white);
    overflow: hidden;
    box-shadow: 0 6px 18px rgba(0,0,0,0.18);
  }
  .card--henry-front { left: 50px;  top: 40px; }
  .card--tom-front   { left: 630px; top: 40px; }
  .card--henry-back  { left: 50px;  top: 410px; }
  .card--tom-back    { left: 630px; top: 410px; }

  /* front */
  .holder { position: absolute; left: 36px; top: 56px; font-family: "Abel", sans-serif; color: var(--name-blue); }
  .holder__name { font-size: 31px; line-height: 1; }
  .holder__role { font-size: 20px; margin-top: 6px; padding-left: 60px; }
  .brand-disc {
    position: absolute; left: 250px; top: 50px;
    width: 200px; height: 200px; border-radius: 50%;
    background: var(--brand-blue);
  }
  .brand-name {
    position: absolute; left: 36px; top: 200px;
    font-family: "Abel", sans-serif; font-size: 17px; color: var(--brand-blue);
  }
  .tagline {
    position: absolute; right: 26px; bottom: 16px;
    font-family: "Reenie Beanie", cursive; font-size: 21px; color: var(--ink);
    white-space: nowrap;
  }

  /* back */
  .back-disc {
    position: absolute; left: 300px; top: 14px;
    width: 330px; height: 330px; border-radius: 50%;
    background: var(--pale-blue); opacity: 0.85;
  }
  .contact { position: absolute; left: 40px; top: 80px; text-align: right; width: 380px; color: var(--ink); }
  .contact p { white-space: nowrap; }
  .contact__phones { font-size: 15px; }
  .contact__web { font-size: 14px; margin-top: 2px; }
  .contact__email { font-size: 14px; margin-top: 14px; }
  .contact__address { font-size: 11px; color: var(--muted); margin-top: 20px; line-height: 1.5; }
  .contact__address span { display: block; }
</style>
</head>
<body>

  <section class="card card--henry-front">
    <div class="holder">
      <p class="holder__name">Henry Walbrook</p>
      <p class="holder__role">Director</p>
    </div>
    <div class="brand-disc"></div>
    <p class="brand-name">Kestrel Office Clearance</p>
    <p class="tagline">free office clearances… hard to beat that, really</p>
  </section>

  <section class="card card--tom-front">
    <div class="holder">
      <p class="holder__name">Tom Pardew</p>
      <p class="holder__role">Director</p>
    </div>
    <div class="brand-disc"></div>
    <p class="brand-name">Kestrel Office Clearance</p>
    <p class="tagline">free office clearances… hard to beat that, really</p>
  </section>

  <section class="card card--henry-back">
    <div class="back-disc"></div>
    <div class="contact">
      <p class="contact__phones">m: 07700 628157 &nbsp; t: 01632 419063</p>
      <p class="contact__web">www.kestrelofficeclearance.co.uk</p>
      <p class="contact__email">henry@kestrelofficeclearance.co.uk</p>
      <p class="contact__address">
        <span>Kestrel Office Clearance, Unit K4 B, 3-7 Ferndale Lane, Harwick</span>
        <span>Linmoor Vale, ZZ9 4QX</span>
      </p>
    </div>
  </section>

  <section class="card card--tom-back">
    <div class="back-disc"></div>
    <div class="contact">
      <p class="contact__phones">m: 07700 513928 &nbsp; t: 01632 419063</p>
      <p class="contact__web">www.kestrelofficeclearance.co.uk</p>
      <p class="contact__email">tom@kestrelofficeclearance.co.uk</p>
      <p class="contact__address">
        <span>Kestrel Office Clearance, Unit K4 B, 3-7 Ferndale Lane, Harwick</span>
        <span>Linmoor Vale, ZZ9 4QX</span>
      </p>
    </div>
  </section>

</body>
</html>
```